Vacation rental Management Software company needs website and logo

We need a logo and new website design to promote our vacation rental management software. We sell the software to property owners and management company. We have existing website www.stayquill.example at the moment but it is need of upgrading. The goal is make it more professional looking and to put the emphasis on marketing the software.
Html + Css code is needed, the website must have responsive layout.
The logo must be composed by the brand "StayQuill" and eventually an image related to Vacation Rental Management
The pages that we need are the following:
1) Home Page
- must be highlighted the 2 main categories of customers (Direct Owners and Agencies/Portals)
- there must be a section where we can highlight some products, i.e. the latest or the most relevant
- there must be an introductive text
2) Page for a category of customer (owner or agency/portal)
- based on the page http://www.stayquill.example/owners/ or http://www.stayquill.example/agencies/, this page must highlight all the products available for the category selected, but must be more attractive then the existing ones (that have just text)
3) Single product page
- in that page must be explained a single product, a page example is this one: http://www.stayquill.example/owners/vacation-rental-website.html
4) Portfolio page
5) Contact page, with a contact form style
Industry/Entity Type
Software

```html
<!DOCTYPE html>
<html lang="en">
<head>
<meta charset="utf-8">
<title>StayQuill – Vacation Rental Management Software</title>
<link href="https://fonts.googleapis.com/css2?family=Ubuntu:wght@400;500;700&family=Open+Sans:wght@400;600&family=PT+Sans:wght@400&display=swap" rel="stylesheet">
<style>
:root{
  --red:#b5121b;
  --red-light:#e0454a;
  --ink:#333;
  --muted:#666;
  --rule:#e2e2e2;
  --nav-top:#3a3a3a;
  --nav-bottom:#0d0d0d;
  --footer:#2b2b2b;
  --footer-bottom:#1e1e1e;
  --footer-text:#d6d6d6;
  --footer-head:#9a9a9a;
  --footer-rule:#444;
}
*{margin:0;padding:0;box-sizing:border-box}
html,body{width:1059px;height:1200px;overflow:hidden;background:#fff}
body{position:relative;font-family:'Open Sans',sans-serif;color:var(--ink)}
a{color:inherit;text-decoration:none}
.abs{position:absolute}

.brand{left:124px;top:48px;font-family:'Ubuntu',sans-serif;font-weight:500;font-size:30px;color:var(--ink);letter-spacing:-.3px}
.top-links{top:31px;left:596px;display:flex;gap:18px;font-family:'Ubuntu',sans-serif;font-size:10px;font-weight:500;color:#222}
.lang-label{left:773px;top:31px;font-size:8.5px;color:#666}
.lang{left:852px;top:26px;width:81px;height:21px;border:1px solid #ccc;border-radius:2px;background:linear-gradient(#fff,#eee);font-size:9px;display:flex;align-items:center;padding-left:7px;gap:6px}
.lang .flag{width:14px;height:9px;background:#2a3f8f;border:1px solid #c8102e}
.search{left:678px;top:78px;width:255px;height:26px;border:1px solid #d8d8d8;border-radius:2px;box-shadow:inset 0 1px 2px rgba(0,0,0,.08);font-size:11px;color:#444;padding:5px 8px}
.search-btn{left:906px;top:78px;width:27px;height:26px;background:var(--red);border-radius:0 2px 2px 0}

.nav{left:125px;top:131px;width:808px;height:38px;background:linear-gradient(var(--nav-top),var(--nav-bottom));border-radius:3px 3px 0 0;border-bottom:3px solid var(--red);display:flex;justify-content:space-between;align-items:center;padding:0 15px;font-family:'Ubuntu',sans-serif;font-weight:500;font-size:12.5px;color:#fff}

.hero{left:125px;top:169px}

.feature-icon{width:82px;height:82px;border-radius:50%;background:#fff;box-shadow:0 1px 4px rgba(0,0,0,.3);display:flex;align-items:center;justify-content:center;flex:none}
.feature-icon span{width:72px;height:72px;border-radius:50%;background:radial-gradient(circle at 50% 35%,var(--red-light),var(--red));display:flex;align-items:center;justify-content:center}
.feature-rule{width:1px;height:95px;background:var(--rule);flex:none}
.feature h2{font-family:'Ubuntu',sans-serif;font-weight:400;font-size:18px;color:#333;margin-bottom:7px}
.feature p{font-size:10px;line-height:14px;color:#666}

.divider-shadow{left:140px;top:686px;width:780px;height:12px;background:radial-gradient(ellipse at 50% 0,rgba(0,0,0,.12),transparent 70%)}

.section-title{left:125px;top:719px;font-family:'Ubuntu',sans-serif;font-weight:400;font-size:18px;color:#333}
.view-all{left:869px;top:718px;width:65px;height:20px;background:#111;border-radius:2px;color:#ef5a5a;font-family:'Ubuntu',sans-serif;font-weight:700;font-size:9px;display:flex;align-items:center;justify-content:center;gap:4px}
.products-rule{left:125px;top:751px;width:808px;height:1px;background:var(--rule)}

.product{top:768px;width:183px;height:150px;border:1px solid #ccc;padding:2px;background:#fff;box-shadow:0 1px 2px rgba(0,0,0,.15)}
.product .photo{width:100%;height:100%;position:relative;overflow:hidden}
.product .label{position:absolute;left:0;right:0;bottom:0;height:36px;background:rgba(30,30,30,.72);display:flex;align-items:center;justify-content:space-between;padding:0 4px 0 11px;color:#fff;font-family:'Ubuntu',sans-serif;font-weight:500;font-size:12.5px}
.product .arrow{width:31px;height:26px;background:#fff;border-radius:2px;display:flex;align-items:center;justify-content:center}

.footer{left:0;top:950px;width:1059px;height:199px;background:var(--footer);font-family:'PT Sans',sans-serif}
.footer h3{position:absolute;top:22px;font-weight:400;font-size:16px;color:var(--footer-head)}
.footer ul{position:absolute;top:51px;list-style:none;font-size:11px;color:var(--footer-text)}
.footer li{height:23px}
.footer .vrule{position:absolute;top:25px;width:1px;height:158px;background:var(--footer-rule)}
.tweet{position:absolute;left:499px;width:232px;font-size:10px;line-height:18px;color:var(--footer-text)}
.tweet small{display:block;font-size:10px;margin-top:4px}
.social{position:absolute;left:817px;top:48px;list-style:none}
.social li{display:flex;align-items:center;gap:11px;height:31px;font-size:11px;color:var(--footer-text)}
.social .dot{width:25px;height:25px;border-radius:50%;background:#f2f2f2;box-shadow:inset 0 -2px 3px rgba(0,0,0,.15)}
.footer-bottom{left:0;top:1149px;width:1059px;height:51px;background:var(--footer-bottom);font-family:'PT Sans',sans-serif;font-size:10px;color:#777;padding:17px 0 0 127px}
</style>
</head>
<body>

<header>
  <div class="abs brand">StayQuill</div>
  <nav class="abs top-links"><a href="#">OWNER LOGIN</a><a href="#">REGISTER NOW</a></nav>
  <div class="abs lang-label">Select Language :</div>
  <div class="abs lang"><span class="flag"></span>English
    <svg width="8" height="6" viewBox="0 0 8 6"><path d="M1 1l3 3 3-3" fill="none" stroke="#333" stroke-width="1.5"/></svg>
  </div>
  <div class="abs search">Search</div>
  <div class="abs search-btn">
    <svg width="27" height="26" viewBox="0 0 27 26"><circle cx="12" cy="11" r="4" fill="none" stroke="#fff" stroke-width="2"/><path d="M15 14l5 5" stroke="#fff" stroke-width="2.5" stroke-linecap="round"/></svg>
  </div>
  <nav class="abs nav"><a href="#">HOME</a><a href="#">PRODUCTS &amp; SERVICES</a><a href="#">PORTFOLIO</a><a href="#">OWNERS</a><a href="#">CONTACT US</a></nav>
</header>

<svg class="abs hero" width="808" height="364" viewBox="0 0 808 364" role="img" aria-label="Photo of a poolside patio table set with bowls and red napkins inside a screened lanai">
  <defs>
    <linearGradient id="heroSky" x1="0" y1="0" x2="0" y2="1">
      <stop offset="0" stop-color="#dfe7ea"/>
      <stop offset=".16" stop-color="#b9c8c4"/>
      <stop offset=".26" stop-color="#6f8158"/>
      <stop offset=".36" stop-color="#8f9a86"/>
      <stop offset=".6" stop-color="#9aa6ad"/>
      <stop offset="1" stop-color="#b29a86"/>
    </linearGradient>
    <radialGradient id="heroPool" cx=".12" cy=".48" r=".35">
      <stop offset="0" stop-color="#5fb8cf" stop-opacity=".8"/>
      <stop offset="1" stop-color="#5fb8cf" stop-opacity="0"/>
    </radialGradient>
    <radialGradient id="heroTable" cx=".52" cy=".62" r=".4">
      <stop offset="0" stop-color="#c4d6e2" stop-opacity=".75"/>
      <stop offset=".7" stop-color="#55636a" stop-opacity=".35"/>
      <stop offset="1" stop-color="#55636a" stop-opacity="0"/>
    </radialGradient>
    <radialGradient id="heroWall" cx=".93" cy=".45" r=".2">
      <stop offset="0" stop-color="#e0d2bd" stop-opacity=".9"/>
      <stop offset="1" stop-color="#e0d2bd" stop-opacity="0"/>
    </radialGradient>
    <clipPath id="heroClip"><path d="M0 0H808V327Q404 395 0 327Z"/></clipPath>
  </defs>
  <g clip-path="url(#heroClip)">
    <rect width="808" height="364" fill="url(#heroSky)"/>
    <rect width="808" height="364" fill="url(#heroPool)"/>
    <rect width="808" height="364" fill="url(#heroTable)"/>
    <rect width="808" height="364" fill="url(#heroWall)"/>
  </g>
  <path d="M0 327Q404 395 808 327" fill="none" stroke="#b5121b" stroke-width="3.5"/>
  <g fill="#b5121b" stroke="#fff" stroke-width="2">
    <circle cx="377" cy="338" r="5"/><circle cx="395" cy="338" r="5"/><circle cx="413" cy="338" r="5"/><circle cx="431" cy="338" r="5"/>
  </g>
</svg>

<section class="abs feature" style="left:125px;top:579px;display:flex;gap:10px;width:420px">
  <div class="feature-icon"><span>
    <svg width="40" height="38" viewBox="0 0 40 38" aria-hidden="true">
      <path d="M20 3L2 18h5v17h26V18h5z" fill="#fff"/>
      <rect x="10" y="21" width="7" height="6" fill="#b5121b"/>
      <rect x="23" y="22" width="7" height="13" fill="#b5121b"/>
    </svg>
  </span></div>
  <div class="feature-rule"></div>
  <div style="width:305px;padding-top:4px">
    <h2>Direct Owners</h2>
    <p>If you want to manage all aspects of your properties, if you want to publish them on the most famous portals, if you want to create websites for your properties, check what we offer!</p>
  </div>
</section>
<section class="abs feature" style="left:560px;top:579px;display:flex;gap:10px;width:380px">
  <div class="feature-icon"><span>
    <svg width="34" height="40" viewBox="0 0 34 40" aria-hidden="true">
      <rect x="6" y="3" width="22" height="35" fill="#fff"/>
      <g fill="#b5121b">
        <rect x="10" y="8" width="5" height="4"/><rect x="19" y="8" width="5" height="4"/>
        <rect x="10" y="15" width="5" height="4"/><rect x="19" y="15" width="5" height="4"/>
        <rect x="10" y="22" width="5" height="4"/><rect x="19" y="22" width="5" height="4"/>
        <rect x="14" y="30" width="6" height="8"/>
      </g>
    </svg>
  </span></div>
  <div class="feature-rule"></div>
  <div style="width:272px;padding-top:4px">
    <h2>Agencies and Portals</h2>
    <p>If you want to manage all aspects of your properties, if you want to publish them on the most famous portals, iyou want to your properties, check what we offer!</p>
  </div>
</section>

<div class="abs divider-shadow"></div>

<h2 class="abs section-title">Latest Products</h2>
<a class="abs view-all" href="#">VIEW ALL <svg width="5" height="6" viewBox="0 0 5 6"><path d="M0 0l5 3-5 3z" fill="#ef5a5a"/></svg></a>
<div class="abs products-rule"></div>

<article class="abs product" style="left:125px"><div class="photo" role="img" aria-label="Photo of a builder shaking hands with a client" style="background:radial-gradient(ellipse at 70% 40%,#e9e2dc 0,transparent 45%),radial-gradient(ellipse at 20% 60%,#7b8fa8 0,transparent 55%),linear-gradient(#c9cfd6,#8c99ab)"><div class="label">VACATION RENTALS<span class="arrow"><svg width="22" height="10" viewBox="0 0 22 10"><path d="M1 1l4 4-4 4M8 1l4 4-4 4M15 1l4 4-4 4" fill="none" stroke="#222" stroke-width="1.6"/></svg></span></div></div></article>
<article class="abs product" style="left:333px"><div class="photo" role="img" aria-label="Photo of hands holding a small model house" style="background:radial-gradient(ellipse at 55% 55%,#e8d0b4 0,transparent 35%),radial-gradient(ellipse at 50% 40%,#d0505a 0,transparent 25%),linear-gradient(#f3d3d8,#dea4ab)"><div class="label">VACATION RENTALS<span class="arrow"><svg width="22" height="10" viewBox="0 0 22 10"><path d="M1 1l4 4-4 4M8 1l4 4-4 4M15 1l4 4-4 4" fill="none" stroke="#222" stroke-width="1.6"/></svg></span></div></div></article>
<article class="abs product" style="left:542px"><div class="photo" role="img" aria-label="Photo of a lit villa with palm trees at dusk" style="background:radial-gradient(ellipse at 50% 70%,#e0a84e 0,transparent 55%),linear-gradient(#23305e,#5a4a3a 50%,#8a6030)"><div class="label">VACATION RENTALS<span class="arrow"><svg width="22" height="10" viewBox="0 0 22 10"><path d="M1 1l4 4-4 4M8 1l4 4-4 4M15 1l4 4-4 4" fill="none" stroke="#222" stroke-width="1.6"/></svg></span></div></div></article>
<article class="abs product" style="left:750px"><div class="photo" role="img" aria-label="Photo of a model house on house plans" style="background:radial-gradient(ellipse at 75% 40%,#e6bf9a 0,transparent 40%),linear-gradient(#f4efe8,#ddd2c4)"><div class="label">VACATION RENTALS<span class="arrow"><svg width="22" height="10" viewBox="0 0 22 10"><path d="M1 1l4 4-4 4M8 1l4 4-4 4M15 1l4 4-4 4" fill="none" stroke="#222" stroke-width="1.6"/></svg></span></div></div></article>

<footer class="abs footer">
  <h3 style="left:127px">COMPANY</h3>
  <ul style="left:127px"><li>Company Overview</li><li>About Us</li><li>Services Provide</li><li>Our Process</li><li>Our Clients</li></ul>
  <div class="vrule" style="left:274px"></div>
  <h3 style="left:315px">WHAT WE DO</h3>
  <ul style="left:315px"><li>Value proposition</li><li>Our work</li><li>Testimonials</li><li>Faq</li><li>Contact us</li></ul>
  <div class="vrule" style="left:458px"></div>
  <h3 style="left:499px;top:20px">CHIRPER FEED</h3>
  <p class="tweet" style="top:49px">Nunc tempus felis vitae urna. Vivamus porttitor, g,<br>purus nisi eleifend libero, a tempus<small>Posted 3 hours ago</small></p>
  <p class="tweet" style="top:121px">Nunc tempus felis vitae urna. Vivamus porttitor, g,<br>purus nisi eleifend libero, a tempus<small>Posted 3 hours ago</small></p>
  <div class="vrule" style="left:769px"></div>
  <h3 style="left:815px;top:20px">GET CONNECTED</h3>
  <ul class="social">
    <li><span class="dot"></span>Circlebook</li>
    <li><span class="dot"></span>Chirper</li>
    <li><span class="dot"></span>WorkLink</li>
    <li><span class="dot"></span>RSS</li>
  </ul>
</footer>
<div class="abs footer-bottom">© 2014 Company Name.&nbsp; All right reserved.&nbsp; Term of Use</div>

</body>
</html>
```